Mobile Marketing Business needs a UNIQUE web design that makes users stop, adore and engage!

Unique web design for a new division of our company. Based in Los Angeles, TornaCell is a mobile marketing company offering mobile optimized websites, sms marketing, strategic and analytic consultation services. We are a b2b model targeting a wide range of industries and business sizes. Our parent company is Harbor Reach Online. Tornacell needs to reflect a progressive nature, confidence, and experience - yet affordable to any business that wants to reach the mobile consumer. We want to avoid a dark website or one that is too bland. The colors should be strong, yet not overly so.

Layout should be clean, focused, - avoiding a cluttered home page. Visitors should recognize WE ARE mobile marketing - it should resonate that WE differ from competitors - Site design should resonate our brand! We've noticed competitors sites start to look and feel like the same - where the visitor may quickly exit from the home page or first inner page. There are some sites that differ which we've listed below.

The audience will range from sophisticated marketers to a local business operator who is not web savvy. The site should welcome all - not intimidate some while wowing others. We understand it's difficult for websites to be a "one size fits all" - but in reviewing competitive sites, it's apparent no one site really leaves any key impression. We'd like Tornacell to be the one.

The site should invite user to engage with the site and compel them to contact us for a demo for a better understanding of how mobiele marketing is the ultimate one 2 one sales channel that can help them improve gross sales.

Site should not be "dark" which requires using white font - we do not want "wild" or "fluorescent" colors. A tasteful, classic balance of colors that provides a comfortable experience to engage.

We realize this challenge seems .. well extremely challenging but we're quite confident there is a "design ninja" lurking out there. Are YOU the one?

Happy to provide more details and info as needed.

Sample sites that we like and feel are unique to the industry and also a site that we feel is quite basic:

www.palvexagency.example - clever use of banner area and using a slider to present services. However, labeling the sliders as such is a little difficult to read.

www.brindlecell.example - clean, classic, minimalistic. Perhaps too minimal for our need but we like it. Nice use of the varying sizes and treatment of 3 promo boxes under main banner. Inner page layout is nice.

www.quarvelworks.example - clever, unique. Love the call to action box (adjacent to phone) offering 3 options for next steps. Inner pages are well designed - overall site is clean, easy to read and merchandises offerings effectively.

www.tallpinegrovemedia.example - clean, well merchandised but home page is a bit too cluttered. good use of colors, inner page layout is simple but effective.

www.wextaline.example - clean, simple easy to follow.

www.plomadix.example - pretty basic site - in fact, you could probably replace the logo with another marketing company, etc. and the site would most likely work. We would prefer to avoid this stigma for TornaCell!!

NOTE: our logo uses a bright green that may limit it's use for mostly accents, etc. We like the contrast of colors used on www.zendravo.example and www.kettlefold.example/ using the dark gray background and other colors to bring some life.

If you google "mobile marketing company", "mobile marketing services", "text messaging services", etc.. you'll notice 2 distinctive categories: amazing - like what the heck were they thinking.. and yawn - like here's another one that looks like the other..

Thank you everyone for the submissions - while they are nice, I have to say they fall into the category we were hoping to avoid (yawn, this one looks like all the other company sites)..  

Please do review the brief thoroughly - we're available if you need a specific issue addressed.  

We're still hoping a design ninja surfaces and provides a comp that makes us go "WOW'..  

cheers and good luck!

Thanks for your participation -  please stay tuned for an update to the brief along with some copy to populate the home page.  

Also... keep an eye on the project award..  we'll be increasing it after posting updates!

cheers.

UPDATE!  We have INCREASED the award in hopes of inspiring you great designers to entice your imagination and creative genetics!

PLEASE feel free to ask for further clarification or even if you want to run something by before submitting a design.  

We also have several other projects and would certainly consider those designers that truly impressed us.

As promised we're adding a bit more detail to this project.  The project requires a home and inner page layout but would like to start with the home page first.   We would also like to have a blog that differs a bit but retain some core elements of the site design.

This is a new design - our desire is to launch a website bearing an effective yet distinctive look.  Again, if you google "mobile marketing services", "mobile marketing company/companies", "mobile ..." aside from the logo varying most of the sites look the same.    We want something different..

The following may be repetitive from our brief but here goes:

Banner will focus on 3 categories - SMS/Text Marketing, Mobile Websites and Mobile Marketing:  
#1)  Headline - Did you notice how many consumers are on smartphones today?  Reach them now. 
Sub text - Mobile coupons get 10 times the redemption rate of traditional coupons
Text messages are read by 94% of recipients within 4 minutes
50% of SMS users are aged 35+ 

#2) Headline - Every day 53% of Americans use their smartphone to search the web.  Do you have a mobile optimized website?   You could be missing all these consumers each day. 
Sub text - 95% of smarthphone users search for local information 
                         70% of all mobile searches result in action within 1 hour
#3) Headline - Break through the clutter - innovative marketing campaigns distinguish your brand
Sub text - Integrate social and mobile campaigns whenever and wherever
 91% of U.S. population have a mobile device within reach 24/7

** We are open to suggestions for images or style of banner - 

Below the banner would like to have a content section featuring rotating messages titled as:
  
DID YOU KNOW? }   There are 5 times as many texters as there are Chatterloop users?   < note 3-4 messages will scroll - a read more text link to an inner page for more of these facts.. 

Need 3 content sections - would prefer atypical format - not boxes, or framed areas but something different - titled:
What is a mobile website?  
Connect with mobile consumers
Mobile marketing revolution

Need:  
** a login icon for clients to access; contact us, email and text message optin - (see reference to Dravix and Quarvelworks sites from prior brief - dravix uses creative fonts for the contact us box and email /sms optin,  quarvelworks uses a creative call to action adjacent to the mobile phone with 3 options)

** to see active/ mouse over effect for navigation
** avoid a really long page - perhaps using scripts to reveal drop down boxes in content sections if necessary. 
** use of complimentary colors - keeping to white with elements of just black and green from logo gets boring
**  interesting yet not distracting shapes
** need to avoid bubble gum or flouorescent colors - note dravix mixes colors in the main banner area in an interesting fashion. 

** need frameless design  

Again, reference the sites we liked .. and didn't like on the original brief.  Additionally we also like these sites:

1) quenlo.example - open, expansive area - uncluttered,

2) http://presskit.harbordaily.example - love the layout and use of the black to emulate ink against white paper tying into the newspaper / brand.  We LOVE LOVE LOVE.. that sort of creativity.. in fact this is perhaps one of our favorite sites and how efficient and unique content sections, buttons, navigation, etc. is 

Looking forward to your submissions - cheers!!   

Reason: Attention all designers - this is the final extension! There are some great comps rolling in so PLEASE get your designs in soon !!!

Target Market(s)

Quite diverse actually - from local businesses (e.g., trades, professional services, retail, restaurant, hospitality, etc.) to agencies.

Industry/Entity Type

Progressive

Requirements
Must have
• Main banner of sort for messaging - would like to present 4-5 key messages that rotate/ fade on topics of SMS, mobile users, etc.
We were wondering if using mobile devices as palvexagency.example did to feature messages - but perhaps this limits amount of text. Also like the www.dravix.example site with the banner rotating but also revealing portions of the slide before and after.

3-4 sections to promote key content that link to inner pages. These will feature some text - e.g., see www.brindlecell.example - creative use of staggering box height and using script to reveal.

Main navigation = Home, Why Mobile, What We Do, Services, News (a blog), Contact. There will be 3-8 subpages for Why mobile, what we do, and services.

Footer - should contain email / text messaging sign up - see www.dravix.example for their optin in design.

Get in Touch- again, love how www.dravix.example has designed the "Get in Touch" call to action - not the typical button shape.

Blog - absolutely

Social icons - chatterloop , workhive, and..?
Nice to have
• Not sure what we'd need here - unless you have an idea. We're open to suggestions despite our strong opinions stated so far..
Should not have
• Avoid:
anything too extreme -
avoid cartoon type illustrations
heavy use of icons
extreme colors
font that is hard to read..

```html
<!DOCTYPE html>
<html lang="en">
<head>
<meta charset="utf-8">
<title>TornaCell – Mobile Marketing</title>
<link href="https://fonts.googleapis.com/css2?family=Ubuntu:wght@300;400;500;700&family=Arimo:wght@400;700&family=Anton&display=swap" rel="stylesheet">
<style>
:root{
  --green:#4a9a22;
  --green-light:#78bd2f;
  --green-dark:#2f7414;
  --ink:#222;
  --text:#4a4a4a;
  --muted:#777;
  --blue:#2a8fc6;
  --footer:#333333;
  --footer-dark:#262626;
  --line:#dcdcdc;
}
*{margin:0;padding:0;box-sizing:border-box}
html,body{width:966px;height:1200px;overflow:hidden}
body{position:relative;font-family:"Arimo",Arial,sans-serif;color:var(--text);
  background:linear-gradient(#f0f7c6 0,#fbfde9 110px,#fff 190px,#fff 445px,#ececec 446px,#fff 520px,#fff 100%)}
.abs{position:absolute}

/* header */
.logo{left:110px;top:14px}
.logo-name{font-family:"Ubuntu",sans-serif;font-weight:500;font-size:46px;color:var(--green);letter-spacing:-1.5px;line-height:1}
.logo-tag{font-family:"Ubuntu",sans-serif;font-size:12.5px;color:#333;letter-spacing:1px;margin-top:2px}
.call{right:107px;top:20px;text-align:right;font-family:"Ubuntu",sans-serif}
.call-line{font-size:15px;font-weight:500;color:#111}
.call-line b{font-size:22px;color:var(--green);font-weight:500;margin-left:6px}
.stay{margin-top:6px;font-size:16px;color:#555;font-style:italic;font-weight:300;display:flex;align-items:center;justify-content:flex-end;gap:4px}
.stay strong{font-style:normal;color:var(--green);font-weight:500;margin-right:6px}
.dot{width:20px;height:20px;border-radius:50%;display:inline-block}

/* nav */
.nav-tail{top:110px;width:0;height:0;border-top:20px solid var(--green-dark);border-bottom:20px solid var(--green-dark)}
.nav-tail.left{left:71px;border-left:30px solid transparent}
.nav-tail.right{left:868px;border-right:30px solid transparent}
.nav{left:101px;top:95px;width:764px;height:44px;background:linear-gradient(#6ab52d,#47991f);
  border-top:2px solid #8fcb4d;box-shadow:0 3px 4px rgba(0,0,0,.25);display:flex;justify-content:space-around;align-items:center}
.nav a{font-family:"Ubuntu",sans-serif;font-size:15px;color:#fff;text-decoration:none}
.nav a:hover{color:#e7f5c8}

/* hero */
.skyline{left:0;top:340px;width:966px;height:105px;background:linear-gradient(#eeeeee,#e0e0e0)}
.arrow{top:238px;width:48px;height:48px;border-radius:50%;background:#d8d8d8}
.hero-title{left:101px;top:222px;font-family:"Ubuntu",sans-serif;font-weight:300;font-size:39px;color:var(--ink);letter-spacing:-1.5px;line-height:44px}
.hero-title em{font-style:normal;color:var(--green)}
.hero-copy{left:105px;top:323px;width:370px;font-family:"Ubuntu",sans-serif;font-size:11.5px;line-height:16px;color:#333}
.btn-start{left:105px;top:376px;width:166px;height:45px;background:linear-gradient(#3fa6dc,#1f7fb5);border:1px solid #1a6e9e;
  color:#fff;font-family:"Ubuntu",sans-serif;font-weight:700;font-size:22px;text-align:center;line-height:43px}
.phones{left:527px;top:205px;width:338px;height:270px;border-radius:18px;background:linear-gradient(90deg,#1c1c1c,#3a3a3a 40%,#5a5a5a 70%,#2a2a2a)}
.badge{left:797px;top:165px;width:96px;height:96px;border-radius:50%;background:radial-gradient(#9ed23f,#5aa51c)}

/* cards */
.card{top:489px;width:216px;height:153px;background:#fafafa;border:1px solid #e2e2e2;box-shadow:0 1px 3px rgba(0,0,0,.15)}
.card-media{position:absolute;left:5px;top:4px;width:204px;height:62px;background:#333}
.card h3{position:absolute;left:9px;top:76px;font-family:"Ubuntu",sans-serif;font-weight:400;font-size:14px;color:#222;letter-spacing:-.3px}
.card h3 span{color:var(--green)}
.card p{position:absolute;left:9px;top:98px;width:202px;font-size:8.3px;line-height:10.5px;color:#555}
.read-more{top:632px;width:100px;height:20px;border-radius:10px;background:linear-gradient(#8ccb3b,#55a11d);
  color:#fff;font-family:"Ubuntu",sans-serif;font-size:8.5px;text-align:center;line-height:20px;box-shadow:0 2px 2px rgba(0,0,0,.15)}

/* about */
.about-title{left:94px;top:677px;font-family:"Ubuntu",sans-serif;font-size:19px;color:#222}
.about-title span{color:var(--green)}
.about-title small{font-size:15px;color:var(--green);margin-left:4px}
.about-copy{left:94px;top:709px;width:485px}
.about-copy p{font-size:9.2px;line-height:16px;color:#555;margin-bottom:16px}
.btn-learn{left:95px;top:906px;width:79px;height:28px;background:#3a3a3a;border:1px solid #222;color:#fff;font-size:10px;font-style:italic;text-align:center;line-height:26px}

/* clients */
.clients-title{left:624px;top:678px;font-family:"Anton",sans-serif;font-size:36px;color:#1d1d1d;letter-spacing:-.5px;line-height:44px}
.clients-sub{left:628px;top:724px;font-family:"Ubuntu",sans-serif;font-size:15px;color:#7a7a7a;letter-spacing:-.5px}
.clients-grid{left:626px;top:747px;width:236px;height:120px;display:grid;grid-template-columns:repeat(3,1fr);grid-template-rows:repeat(2,1fr)}
.client{display:flex;align-items:center;justify-content:center;font-family:"Ubuntu",sans-serif;font-size:11px;font-weight:500;color:#444}
.client:nth-child(-n+3){border-bottom:1px solid var(--line)}
.client:not(:nth-child(3n)){border-right:1px solid var(--line)}

/* get in touch band */
.touch{left:0;top:958px;width:966px;height:40px;background:linear-gradient(#6db92e,#3f8e1a)}
.touch-phone{left:155px;top:949px;width:66px;height:50px;border-radius:8px;background:linear-gradient(#555,#1e1e1e);transform:rotate(-12deg)}
.touch-label{left:236px;top:964px;font-family:"Ubuntu",sans-serif;font-weight:300;font-size:20px;color:#fff}
.field{top:968px;height:22px;background:#fff;border:1px solid #cfcfcf;font-size:10px;font-style:italic;color:#aaa;padding-left:9px;line-height:20px}
.btn-submit{left:711px;top:968px;width:54px;height:22px;background:#1e1e1e;color:#fff;font-size:10.5px;font-style:italic;text-align:center;line-height:22px}

/* footer */
.footer{left:0;top:998px;width:966px;height:161px;background:var(--footer)}
.col{top:1015px}
.col h4{font-family:"Ubuntu",sans-serif;font-weight:400;font-size:14.5px;color:#fff;margin-bottom:5px}
.col li{list-style:none;font-size:8.8px;color:#eee;line-height:19.3px}
.foot-logo{left:648px;top:1044px}
.foot-logo .logo-name{font-size:44px;color:var(--green-light)}
.foot-logo .logo-tag{color:#fff;font-size:12px}
.bottom{left:0;top:1159px;width:966px;height:41px;background:var(--footer-dark)}
.legal{left:118px;top:1172px;font-size:8.6px;color:#eee}
.legal span{margin:0 9px}
.connect{left:711px;top:1169px;display:flex;align-items:center;gap:5px;font-family:"Ubuntu",sans-serif;font-weight:300;font-size:12.5px;color:#fff}
.sq{width:17px;height:17px;border-radius:3px;display:inline-block}
</style>
</head>
<body>

<header>
  <div class="abs logo">
    <div class="logo-name">tornacell</div>
    <div class="logo-tag">MAKE YOUR BRAND TORNA.MOBI</div>
  </div>
  <div class="abs call">
    <div class="call-line">CALL NOW! <b>1-800-000-0000</b></div>
    <div class="stay">let's stay <strong>Connected!</strong>
      <span class="dot" style="background:#2b4e93"></span>
      <span class="dot" style="background:#3aa7dd"></span>
      <span class="dot" style="background:#1e6ea8"></span>
      <span class="dot" style="background:#e8741f"></span>
    </div>
  </div>
</header>

<div class="abs nav-tail left"></div>
<div class="abs nav-tail right"></div>
<nav class="abs nav">
  <a href="#">Home</a><a href="#">Why Mobile</a><a href="#">What We Do</a><a href="#">Services</a><a href="#">News</a><a href="#">Contact</a>
</nav>

<section class="hero">
  <div class="abs skyline" role="img" aria-label="Pale grey city skyline silhouette"></div>
  <div class="abs arrow" style="left:19px">
    <svg width="48" height="48"><path d="M28 14 L18 24 L28 34" fill="none" stroke="#fff" stroke-width="3"/></svg>
  </div>
  <div class="abs arrow" style="left:898px">
    <svg width="48" height="48"><path d="M20 14 L30 24 L20 34" fill="none" stroke="#fff" stroke-width="3"/></svg>
  </div>
  <h1 class="abs hero-title">Consumers are <em>mobile</em>.<br><em>Are You?</em></h1>
  <p class="abs hero-copy">Mobile has forever altered the way people read, purchase goods, play games and engage with their lives. It's time to get mobile.</p>
  <div class="abs btn-start">Get Started</div>
  <div class="abs phones" role="img" aria-label="Row of five smartphones showing app screens"></div>
  <div class="abs badge" role="img" aria-label="Green starburst badge reading Smart Services"></div>
</section>

<section class="cards">
  <article class="abs card" style="left:133px">
    <div class="card-media" role="img" aria-label="Chalkboard with the words Mobile Marketing"></div>
    <h3><span>SMS</span> Marketing</h3>
    <p>Lorem ipsum dolor sit amet, consectetur adipiscing elit. Sed sagittis consectetur nunc in blandit. Donec aliquam, lacus vel semper congue, sem tellus</p>
  </article>
  <div class="abs read-more" style="left:191px">Read More</div>

  <article class="abs card" style="left:373px">
    <svg class="card-media" style="background:#fff;border:1px solid #ddd" viewBox="0 0 204 62" role="img" aria-label="Colourful bar chart">
      <g>
        <rect x="12" y="8" width="4" height="54" fill="#f3c600"/><rect x="17" y="16" width="4" height="46" fill="#7cc242"/><rect x="22" y="30" width="4" height="32" fill="#4aa3df"/><rect x="27" y="40" width="4" height="22" fill="#f26522"/>
        <rect x="40" y="40" width="4" height="22" fill="#f3c600"/><rect x="45" y="44" width="4" height="18" fill="#e53935"/><rect x="50" y="48" width="4" height="14" fill="#1f9c8c"/><rect x="55" y="44" width="4" height="18" fill="#f26522"/>
        <rect x="68" y="44" width="4" height="18" fill="#1f9c8c"/><rect x="73" y="40" width="4" height="22" fill="#888"/><rect x="78" y="18" width="4" height="44" fill="#7cc242"/><rect x="83" y="50" width="4" height="12" fill="#f3c600"/>
        <rect x="96" y="40" width="4" height="22" fill="#4aa3df"/><rect x="101" y="54" width="4" height="8" fill="#f26522"/><rect x="106" y="50" width="4" height="12" fill="#e53935"/>
        <rect x="130" y="30" width="4" height="32" fill="#555"/><rect x="140" y="20" width="4" height="42" fill="#7cc242"/><rect x="145" y="16" width="4" height="46" fill="#4aa3df"/><rect x="150" y="14" width="4" height="48" fill="#f26522"/>
        <rect x="165" y="24" width="4" height="38" fill="#f3c600"/><rect x="175" y="14" width="4" height="48" fill="#1f9c8c"/><rect x="180" y="22" width="4" height="40" fill="#e53935"/><rect x="185" y="24" width="4" height="38" fill="#888"/>
      </g>
    </svg>
    <h3><span>Strategic</span> and Analytic</h3>
    <p>Lorem ipsum dolor sit amet, consectetur adipiscing elit. Sed sagittis consectetur nunc in blandit. Donec aliquam, lacus vel semper congue, sem tellus</p>
  </article>
  <div class="abs read-more" style="left:424px">Read More</div>

  <article class="abs card" style="left:614px">
    <div class="card-media" style="background:linear-gradient(#f4f4f4,#dcdcdc)" role="img" aria-label="Workshop promo banner with rows of app icons"></div>
    <h3><span>Marketing</span> Review</h3>
    <p>Lorem ipsum dolor sit amet, consectetur adipiscing elit. Sed sagittis consectetur nunc in blandit. Donec aliquam, lacus vel semper congue, sem tellus</p>
  </article>
  <div class="abs read-more" style="left:669px">Read More</div>
</section>

<section class="about">
  <h2 class="abs about-title"><span>T</span>orna Cell <small>Make Your Brand Torna.mobi</small></h2>
  <div class="abs about-copy">
    <p>Lorem ipsum dolor sit amet, consectetur adipiscing elit. Sed sagittis consectetur nunc in blandit. Donec aliquam, lacus vel semper congue, sem tellus tincidunt turpis, a vehicula leo tellus quis enim. Mauris dolor ligula, semper vel ullamcorper nec, sollicitudin non erat. Pellentesque bibendum, ipsum sed placerat ultrices, urna quam aliquam lectus, et consequat mauris enim sit amet mi. Donec ultricies dolor quis urna pharetra id condimentum sem venenatis.</p>
    <p>Praesent ac sem sed erat rhoncus viverra ac sit amet nibh. Vestibulum iaculis dolor ut sem accumsan at consequat mi gravida. Nullam vel justo nulla. Quisque lobortis fermentum consectetur. Pellentesque pretium nisi quis lacus ornare consequat sit amet dignissim nisl.</p>
    <p>Mauris rhoncus, quam in dignissim accumsan, est magna egestas mauris, quis ultricies ligula massa eu mauris. Suspendisse tempor neque eu nulla consectetur sollicitudin.</p>
  </div>
  <div class="abs btn-learn">Learn More..</div>
</section>

<section class="clients">
  <h2 class="abs clients-title">OUR CLIENTS</h2>
  <div class="abs clients-sub">TRUST US WITH THEIR CUSTOMERS</div>
  <div class="abs clients-grid">
    <div class="client">Farelane</div>
    <div class="client">Tradeharbor</div>
    <div class="client">Stylecove</div>
    <div class="client">Vowpath</div>
    <div class="client">Deskwell</div>
    <div class="client">Tinysprout</div>
  </div>
</section>

<section class="get-in-touch">
  <div class="abs touch"></div>
  <div class="abs touch-phone" role="img" aria-label="Smartphone showing an envelope"></div>
  <div class="abs touch-label">Get in touch:</div>
  <div class="abs field" style="left:357px;width:164px">Name</div>
  <div class="abs field" style="left:532px;width:165px">E-mail</div>
  <div class="abs btn-submit">Submit</div>
</section>

<footer>
  <div class="abs footer"></div>
  <div class="abs col" style="left:114px"><h4>About</h4><ul><li>Our Team</li><li>In the News</li><li>Case Studies</li></ul></div>
  <div class="abs col" style="left:250px"><h4>Resources</h4><ul><li>Blog</li><li>Industry Stats</li><li>White Papers</li></ul></div>
  <div class="abs col" style="left:393px"><h4>Solutions</h4><ul><li>Mobile CRM</li><li>Mobile Coupons</li><li>Tornacell Surveys</li><li>Industry Solutions</li><li>Custom Solutions</li></ul></div>
  <div class="abs col" style="left:534px"><h4>Platforms</h4><ul><li>Tornacell Studio</li><li>Tornacell Spark</li><li>Tornacell Classifieds</li><li>Tornacell Climate</li><li>Nest4Cell</li><li>The Third Tier</li></ul></div>
  <div class="abs foot-logo">
    <div class="logo-name">tornacell</div>
    <div class="logo-tag">MAKE YOUR BRAND TORNA.MOBI</div>
  </div>
  <div class="abs bottom"></div>
  <div class="abs legal">Privacy Policy<span>|</span>Terms &amp; Conditions</div>
  <div class="abs connect">Stay Connected:
    <span class="sq" style="background:#3b5a9a"></span>
    <span class="sq" style="background:#3aa7dd"></span>
    <span class="sq" style="background:#1e6ea8"></span>
  </div>
</footer>

</body>
</html>
```